Rate sheet redesign

We provide rate sheets to agents for our scenic flights and I would like to make them easier to read and more comprehensive. I'd also like to be able to edit the information in the design, as tours get updated and so do the rates. We've got new product out of shark bay, so the sections would need to be: Perth, Geraldton, Kalbarri and Shark Bay. I've attached what we've been using and also some concept photos.

also a link to our flights online: https://coralwingtours.bookvista.com/catalog/418752/flights-from-perth

I've put this under brochure redesign as I wasn't sure what a rate sheet would be considered. Open to different formats if it means content is editable.

Need extra days to review

```html
<!DOCTYPE html>
<html lang="en">
<head>
<meta charset="utf-8">
<title>25/26 Rates Retail – Coralwing Aviation</title>
<link href="https://fonts.googleapis.com/css2?family=Poppins:wght@400;500;600;700;800&display=swap" rel="stylesheet">
<style>
  :root {
    --navy: #0b4f93;
    --navy-dark: #0a3f7a;
    --orange: #ef9a26;
    --sky: #2fa6e6;
    --white: #ffffff;
    --ink: #1c2a3a;
    --canvas: #ffffff;
  }
  * { box-sizing: border-box; margin: 0; padding: 0; }
  html, body { width: 924px; height: 1200px; overflow: hidden; background: var(--canvas); }
  body { font-family: "Poppins", sans-serif; color: var(--ink); position: relative; }

  .sheet {
    position: absolute; left: 106px; width: 712px; height: 503px;
    overflow: hidden; box-shadow: 0 6px 24px rgba(20, 30, 50, .12);
  }
  .sheet--contents { top: 82px; }
  .sheet--geraldton { top: 615px; }

  .sheet__backdrop { position: absolute; inset: 0; }
  .sheet--contents .sheet__backdrop {
    background: linear-gradient(180deg, #ffffff 0%, #f4f8fc 22%, #cfe4f6 36%, #4b9ee0 52%, #1b6fcc 70%, #0d4fae 100%);
  }
  .sheet--geraldton .sheet__backdrop {
    background:
      linear-gradient(90deg, rgba(0,0,0,0) 78%, rgba(196,150,104,.85) 95%),
      linear-gradient(180deg, #ffffff 0%, #f3f8fb 22%, #bfe6ef 42%, #4fbfd6 62%, #2a8ea6 80%, #1f5f74 100%);
  }

  .sheet__title {
    position: absolute; left: 34px; color: var(--navy);
    font-weight: 800; line-height: 1; letter-spacing: -1.5px; white-space: nowrap;
  }
  .sheet--contents .sheet__title { top: 48px; font-size: 47px; }
  .sheet--geraldton .sheet__title { top: 28px; font-size: 46px; letter-spacing: -1px; }

  .sheet__subtitle {
    position: absolute; left: 36px; top: 76px; width: 460px;
    color: var(--navy); font-weight: 700; font-size: 14.5px; line-height: 18px; letter-spacing: -.2px;
  }

  .brand {
    position: absolute; left: 548px; top: 38px; width: 130px;
    display: flex; flex-direction: column; align-items: center; gap: 6px;
  }
  .brand__dot { width: 30px; height: 30px; border-radius: 50%; background: var(--navy); }
  .brand__name {
    color: var(--navy); font-weight: 600; font-size: 16px; line-height: 18px; text-align: center;
  }

  .page-number {
    position: absolute; left: 664px; width: 13px; height: 13px; border-radius: 50%;
    background: var(--orange); color: var(--white); font-size: 6px; font-weight: 700;
    display: flex; align-items: center; justify-content: center;
  }

  /* Contents table */
  .contents {
    position: absolute; left: 91px; top: 142px; width: 530px;
    display: grid; grid-template-columns: 126px 245px 159px; row-gap: 4px;
    font-size: 8px;
  }
  .contents__head {
    height: 41px; display: flex; align-items: center; justify-content: center;
    color: var(--white); font-weight: 700; font-size: 14.5px; letter-spacing: .2px;
  }
  .contents__head--orange { background: var(--orange); }
  .contents__head--navy { background: var(--navy); }
  .contents__cell {
    height: 40.5px; display: flex; align-items: center; justify-content: center; text-align: center;
    line-height: 10px;
  }
  .contents__location { background: var(--navy); color: var(--white); font-weight: 700; font-size: 7.5px; }
  .contents__address { background: var(--white); color: var(--ink); }
  .contents__pages { background: var(--navy); color: var(--white); }
  .contents__terms { grid-column: 1 / 3; background: var(--white); font-weight: 700; font-size: 7.5px; color: var(--navy-dark); }
  .contents__rule { grid-column: 1 / 4; height: 0; }

  /* Rates table */
  .rates {
    position: absolute; left: 56px; top: 131px; width: 600px;
  }
  .rates__head, .rates__row {
    display: grid; grid-template-columns: 107px 224px 124px 72px 73px;
  }
  .rates__head { height: 43px; gap: 1px; }
  .rates__head span {
    display: flex; align-items: center; justify-content: center;
    color: var(--white); font-weight: 700; font-size: 14.5px;
  }
  .rates__head .is-navy { background: var(--navy); }
  .rates__head .is-orange { background: var(--orange); }

  .rates__row { height: 77px; margin-top: 9px; font-size: 8.4px; line-height: 10.2px; }
  .rates__row:first-of-type { margin-top: 8px; }
  .rates__row--light { background: var(--white); color: var(--ink); }
  .rates__row--dark { background: var(--navy); color: var(--white); border: 1px solid var(--white); }
  .rates__row--dark > div + div { border-left: 1px solid var(--white); }
  .rates__row > div { display: flex; flex-direction: column; justify-content: center; }
  .rates__flight { padding-left: 13px; }
  .rates__inclusions { padding-left: 13px; padding-right: 6px; }
  .rates__clauses { padding-left: 11px; padding-right: 4px; }
  .rates__price { align-items: center; }
  .rates__label { color: var(--orange); font-weight: 600; }
  .rates__gap { height: 6px; }

  .rates-note {
    position: absolute; left: 40px; top: 456px; width: 640px;
    color: var(--white); font-weight: 700; font-size: 7.6px; line-height: 10px; text-align: center;
  }
</style>
</head>
<body>

<section class="sheet sheet--contents">
  <div class="sheet__backdrop" role="img" aria-label="Aerial photograph from an aircraft window over blue ocean, coral islands and a wing tip"></div>
  <h1 class="sheet__title">25/26 RATES RETAIL</h1>
  <div class="brand">
    <span class="brand__dot"></span>
    <span class="brand__name">Coralwing<br>Aviation</span>
  </div>

  <div class="contents">
    <div class="contents__head contents__head--orange">LOCATION</div>
    <div class="contents__head contents__head--navy">ADDRESS</div>
    <div class="contents__head contents__head--orange">PAGES</div>

    <div class="contents__cell contents__location">GERALDTON</div>
    <div class="contents__cell contents__address">14 Runway Rise,<br>Moonyoonooka WA 6532</div>
    <div class="contents__cell contents__pages">2–5</div>

    <div class="contents__cell contents__location">GERALDTON - KALBARRI<br>(ONLY AVAILABLE<br>TO AGENTS)</div>
    <div class="contents__cell contents__address">14 Runway Rise,<br>Moonyoonooka WA 6532</div>
    <div class="contents__cell contents__pages">6</div>

    <div class="contents__cell contents__location">KALBARRI</div>
    <div class="contents__cell contents__address">Hangar 2, Reef Drive,<br>Kalbarri WA 6536</div>
    <div class="contents__cell contents__pages">7–10</div>

    <div class="contents__cell contents__location">PERTH</div>
    <div class="contents__cell contents__address">Southgate Airfield</div>
    <div class="contents__cell contents__pages">11–13</div>

    <div class="contents__cell contents__terms">TERMS AND CONDITIONS</div>
    <div class="contents__cell contents__pages">14</div>
  </div>

  <span class="page-number" style="top:458px">01</span>
</section>

<section class="sheet sheet--geraldton">
  <div class="sheet__backdrop" role="img" aria-label="Aerial photograph of turquoise sea meeting a sandy coastline"></div>
  <h1 class="sheet__title">GERALDTON RATES</h1>
  <p class="sheet__subtitle">TOUR RATES VALID FROM 1ST APRIL 2025 TO 31ST MARCH 2026 – RETAIL RATES</p>
  <div class="brand">
    <span class="brand__dot"></span>
    <span class="brand__name">Coralwing<br>Aviation</span>
  </div>

  <div class="rates">
    <div class="rates__head">
      <span class="is-navy">FLIGHT</span>
      <span class="is-orange">INCLUSIONS</span>
      <span class="is-navy">CLAUSES</span>
      <span class="is-orange">ADULT</span>
      <span class="is-navy">CHILD</span>
    </div>

    <div class="rates__row rates__row--light">
      <div class="rates__flight">Abrolhos Island<br>Discovery Tour<br>(Flight 303)</div>
      <div class="rates__inclusions">
        <p><span class="rates__label">Included:</span> Scenic flight from Geraldton to East Wallabi Island return. Morning /Afternoon Tea, and snorkel gear.</p>
        <div class="rates__gap"></div>
        <p><span class="rates__label">Duration:</span> 1 hour 20 minutes flight time<br>5 hours 30 minutes Total Tour time</p>
      </div>
      <div class="rates__clauses">Normal departure time is 8am, however timing is flexible depending on bookings. Start time must be 6 hours before sunset.</div>
      <div class="rates__price">$550.00</div>
      <div class="rates__price">$385.00</div>
    </div>

    <div class="rates__row rates__row--dark">
      <div class="rates__flight">Abrolhos Island<br>Discovery Tour plus<br>Pink Lake (Flight 304)</div>
      <div class="rates__inclusions">
        <p><span class="rates__label">Included:</span> Scenic flight from Geraldton to East Wallabi Island return via Pink Lake. Morning/Afternoon Tea, and snorkel gear.</p>
        <p><span class="rates__label">Duration:</span> 2 hours flight time<br>6 hours Total Tour time</p>
      </div>
      <div class="rates__clauses">Normal departure time is 8am, however timing is flexible depending on bookings. Start time must be 6 hours before sunset.</div>
      <div class="rates__price">$610.00</div>
      <div class="rates__price">$427.00</div>
    </div>

    <div class="rates__row rates__row--light">
      <div class="rates__flight">Abrolhos Islands<br>&amp; Batavia Shipwreck<br>(Flight 303B)</div>
      <div class="rates__inclusions">
        <p><span class="rates__label">Included:</span> Scenic flight from Geraldton to East Wallabi Island return, and Morning /Afternoon Tea</p>
        <div class="rates__gap"></div>
        <p><span class="rates__label">Duration:</span> 1 hour 20 minutes flight time<br>2 hours Total Tour time</p>
      </div>
      <div class="rates__clauses">Normal departure time is 2pm, however timing is flexible depending on bookings. Start time must be 2.5 hours before sunset.</div>
      <div class="rates__price">$500.00</div>
      <div class="rates__price">$350.00</div>
    </div>
  </div>

  <p class="rates-note">PLEASE NOTE THERE IS A NEW $11 GOVERNMENT FEE FOR ALL FLIGHTS LANDING AT THE ABROLHOS ISLANDS, THIS IS NOT A COMMISSIONABLE FEE<br>AND NEEDS TO BE PAID ON TOP OF THE NETT RATE</p>

  <span class="page-number" style="top:456px">02</span>
</section>

</body>
</html>
```